Corporate Brightfen business cards to be handed to investor, bankers etc. Needs to have a young feel

I need business cards designed for a technology company that provides uber-like rapid response on the security industry. I would like it simple but very cool and tasteful. See attached documents for artwork and colours to be used. Cut sheet describes business model. Card stock should be thicker than normal. I would like the one side to be just the art and the other to have the contact info with maybe the pin somewhere.

Target Market(s)

Investors

Industry/Entity Type

Business

Contact Information for Business Card

Would like the logo attached on one side with name address and other info on the other side.

Font styles to use
Other font styles liked:
• See existing logo

Colors
6b449b
886aae
e4daeb
ffffff

Requirements
Must have
• Name: Dorian Felkatsis
• Address: 47 Larkfield Avenue, Toronto, On, M6K2B7
• Tel: 416-7291846
• Email: rolo@brightfen.io
Nice to have
• See logo colours

```html
<!DOCTYPE html>
<html lang="en">
<head>
<meta charset="utf-8">
<title>Brightfen Business Cards</title>
<link href="https://fonts.googleapis.com/css2?family=Jost:wght@400&family=Oswald:wght@300;400&display=swap" rel="stylesheet">
<style>
  :root {
    --purple: #6b449b;
    --purple-soft: #886aae;
    --lilac: #e4daeb;
    --white: #ffffff;
    --ink: #1a1a1a;
    --card-dark: #121212;
    --backdrop: #eeeef0;
  }
  * { margin: 0; padding: 0; box-sizing: border-box; }
  html, body {
    width: 1200px;
    height: 863px;
    overflow: hidden;
    background: var(--backdrop);
  }
  .stage {
    position: relative;
    width: 1200px;
    height: 863px;
    display: flex;
    justify-content: center;
    align-items: center;
    gap: 60px;
  }
  .card {
    position: relative;
    width: 300px;
    height: 525px;
    box-shadow: 0 6px 24px rgba(0, 0, 0, 0.12);
    overflow: hidden;
  }

  /* Front side */
  .card-front {
    background: var(--card-dark);
  }
  .card-front .edge-top,
  .card-front .edge-bottom {
    position: absolute;
    left: 0;
    width: 300px;
  }
  .card-front .edge-top { top: 0; height: 30px; }
  .card-front .edge-bottom { bottom: 0; height: 30px; }
  .card-front .photo-area {
    position: absolute;
    top: 18px;
    bottom: 16px;
    left: 0;
    right: 0;
    background:
      radial-gradient(ellipse at 60% 35%, #3a3a3a 0%, rgba(40,40,40,0) 55%),
      radial-gradient(ellipse at 35% 75%, #2a2a2a 0%, rgba(30,30,30,0) 50%),
      linear-gradient(160deg, #1d1d1d 0%, #0c0c0c 100%);
  }
  .card-front .wordmark {
    position: absolute;
    top: 236px;
    left: 0;
    right: 0;
    display: flex;
    justify-content: center;
    align-items: center;
    gap: 8px;
  }
  .wordmark .mark-dot {
    width: 16px;
    height: 16px;
    border-radius: 50%;
    background: var(--purple-soft);
  }
  .wordmark .brand-name {
    font-family: 'Jost', sans-serif;
    font-weight: 400;
    font-size: 38px;
    letter-spacing: -0.5px;
    color: var(--white);
    text-transform: lowercase;
  }

  /* Back side */
  .card-back {
    background: var(--white);
    text-align: center;
    color: var(--ink);
  }
  .card-back .pin-dot {
    width: 18px;
    height: 18px;
    border-radius: 50%;
    background: var(--purple);
    margin: 118px auto 0;
  }
  .card-back .person-name {
    font-family: 'Oswald', sans-serif;
    font-weight: 300;
    font-size: 17px;
    letter-spacing: 0.3px;
    text-transform: uppercase;
    margin-top: 14px;
  }
  .card-back .contact {
    font-family: 'Jost', sans-serif;
    font-size: 14px;
    line-height: 1.35;
    font-style: normal;
  }
  .card-back .address { margin-top: 26px; }
  .card-back .reach { margin-top: 22px; }
</style>
</head>
<body>
<main class="stage">
  <section class="card card-front" aria-label="Card front">
    <div class="photo-area" role="img" aria-label="Dark, softly blurred photograph of a building interior"></div>
    <svg class="edge-top" viewBox="0 0 300 30" aria-hidden="true">
      <path d="M0 0 H300 V18 H130 L122 26 L114 18 H0 Z" fill="var(--white)"/>
    </svg>
    <svg class="edge-bottom" viewBox="0 0 300 30" aria-hidden="true">
      <path d="M0 30 H300 V14 H228 L220 6 L212 14 H0 Z" fill="var(--purple)"/>
    </svg>
    <div class="wordmark">
      <span class="mark-dot" aria-hidden="true"></span>
      <span class="brand-name">Brightfen</span>
    </div>
  </section>

  <section class="card card-back" aria-label="Card back">
    <div class="pin-dot" aria-hidden="true"></div>
    <h1 class="person-name">Dorian Felkatsis</h1>
    <address class="contact address">
      47 Larkfield Avenue<br>
      Toronto, On, M6K2B7
    </address>
    <p class="contact reach">
      416-7291846<br>
      rolo@brightfen.io<br>
      www.brightfen.io
    </p>
  </section>
</main>
</body>
</html>
```